New Business Card Design Project

Looking for a modern business card design for an import distribution business for industrial technical products. The winning design will translate modern, sophistication, technical, professional and sustainable.

Target Market(s)

Technical customers

Industry/Entity Type

Business

Contact Information for Business Card

Dean Harlow
Sales Manager
M: 0471 625 183
P: 1300 872 619
dean@volkarsystems.com.au
4/18 Galloway Crest Road
Kellbrook NSW 2147
www.volkarsystems.com.au

Font styles to use
Sans Serif

Colors
ec1f27
606060
000000
fbfbfb

Requirements
Must have
• My Logo which is the Volkar Systems logo attached
Nice to have
• Eurostile Bold font

```html
<!DOCTYPE html>
<html lang="en">
<head>
<meta charset="utf-8">
<title>Volkar Systems – Business Card</title>
<link rel="stylesheet" href="https://fonts.googleapis.com/css2?family=Michroma&family=Saira:wght@500;600&display=swap">
<style>
  :root {
    --red: #e0302a;
    --grey: #6b6e73;
    --card: #231f20;
    --white: #fbfbfb;
    --email: #b9bbbe;
    --backdrop: #e9e7e4;
  }
  * { margin: 0; padding: 0; box-sizing: border-box; }
  html, body { width: 1200px; height: 900px; overflow: hidden; }
  body {
    background: var(--backdrop);
    display: flex;
    flex-direction: column;
    align-items: center;
    justify-content: center;
    gap: 36px;
    font-family: "Saira", sans-serif;
  }
  .card {
    position: relative;
    width: 660px;
    height: 400px;
    background: var(--card);
    box-shadow: 0 10px 24px rgba(0,0,0,.25);
    overflow: hidden;
  }

  /* front */
  .brand {
    position: absolute;
    top: 36px; left: 0; right: 0;
    display: flex;
    align-items: center;
    justify-content: center;
    gap: 16px;
  }
  .brand-square { width: 44px; height: 44px; background: var(--red); }
  .brand-name {
    font-family: "Michroma", sans-serif;
    font-size: 29px;
    color: var(--red);
    letter-spacing: 1px;
    text-transform: uppercase;
    white-space: nowrap;
  }
  .holder {
    position: absolute;
    top: 120px; left: 0; right: 0;
    text-align: center;
  }
  .holder-name {
    font-family: "Michroma", sans-serif;
    font-weight: 400;
    font-size: 27px;
    line-height: 1.2;
    color: var(--white);
    letter-spacing: 1px;
    text-transform: uppercase;
  }
  .holder-role {
    font-size: 20px;
    font-weight: 600;
    color: var(--grey);
    letter-spacing: .5px;
    margin-top: 2px;
  }
  .contact-band {
    position: absolute;
    top: 218px; left: 0; right: 0;
    height: 82px;
    background: var(--red);
    display: flex;
    align-items: center;
    justify-content: space-between;
    padding: 0 44px 0 112px;
    color: var(--white);
    font-weight: 600;
  }
  .phones { font-size: 21px; line-height: 1.3; }
  .phones li { list-style: none; display: flex; align-items: center; gap: 12px; }
  .icon-dot {
    width: 24px; height: 24px; border-radius: 50%;
    background: var(--white);
    display: inline-flex; align-items: center; justify-content: center;
    flex: none;
  }
  .address { font-size: 19px; line-height: 1.3; white-space: nowrap; }
  .tab-edges { position: absolute; top: 300px; left: 0; }
  .email {
    position: absolute;
    top: 310px; left: 0; right: 0;
    display: flex; justify-content: center; align-items: center; gap: 10px;
    font-size: 20px; font-weight: 500;
    color: var(--email);
    letter-spacing: .3px;
  }

  /* back */
  .back-mark {
    position: absolute;
    top: 62px; left: 0; right: 0;
    display: flex; flex-direction: column; align-items: center; gap: 24px;
  }
  .back-square { width: 170px; height: 170px; background: var(--red); }
  .back-name {
    font-family: "Michroma", sans-serif;
    font-size: 24px;
    color: var(--grey);
    letter-spacing: 2px;
    text-transform: uppercase;
    white-space: nowrap;
  }
  .website {
    position: absolute;
    bottom: 40px; left: 0; right: 0;
    text-align: center;
    font-size: 24px; font-weight: 600;
    color: var(--grey);
  }
  .website .domain { color: var(--red); }
</style>
</head>
<body>

<section class="card card-front">
  <div class="brand">
    <span class="brand-square"></span>
    <span class="brand-name">Volkar Systems</span>
  </div>

  <div class="holder">
    <h1 class="holder-name">Dean Harlow</h1>
    <p class="holder-role">Sales Manager</p>
  </div>

  <div class="contact-band">
    <ul class="phones">
      <li>
        <span class="icon-dot">
          <svg width="12" height="14" viewBox="0 0 12 14"><rect x="2" y="0.5" width="8" height="13" rx="1.5" fill="none" stroke="#e0302a" stroke-width="1.6"/><circle cx="6" cy="11" r="1" fill="#e0302a"/></svg>
        </span>
        0471 625 183
      </li>
      <li>
        <span class="icon-dot">
          <svg width="14" height="14" viewBox="0 0 14 14"><path d="M3 1l2.5 3-1.4 1.6c.8 1.7 2.1 3 3.8 3.8L9.5 8 13 10.5 11.5 13C6 13 1 8 1 2.5z" fill="#e0302a"/></svg>
        </span>
        1300 872 619
      </li>
    </ul>
    <p class="address">4/18 Galloway Crest Road<br>Kellbrook NSW</p>
  </div>

  <svg class="tab-edges" width="660" height="100" viewBox="0 0 660 100" aria-hidden="true">
    <line x1="168" y1="0" x2="108" y2="64" stroke="#e0302a" stroke-width="4"/>
    <line x1="598" y1="0" x2="538" y2="64" stroke="#e0302a" stroke-width="4"/>
  </svg>

  <p class="email">
    <span class="icon-dot">
      <svg width="14" height="10" viewBox="0 0 14 10"><rect x="0.5" y="0.5" width="13" height="9" fill="#e0302a"/><polyline points="0.5,0.5 7,5.5 13.5,0.5" fill="none" stroke="#fbfbfb" stroke-width="1.2"/></svg>
    </span>
    dean@volkarsystems.com.au
  </p>
</section>

<section class="card card-back">
  <div class="back-mark">
    <span class="back-square"></span>
    <span class="back-name">Volkar Systems</span>
  </div>
  <p class="website">www.<span class="domain">volkarsystems</span>.com.au</p>
</section>

</body>
</html>
```